Web Design Project for an operational risk management consulting company

Website is for a consulting company specialising in operational risk management. Our specialist areas include crisis and emergency management, community engagement, safety and security. We work internationally, generally in high hazard environments. We are a highly ethical and professional company which prides itself on delivering a strong level of customer service.

As a company we recognise that the key to keeping people safe is ensuring that they work in an ethical and sustainable manner. Therefore we are as much about soft skills as we are about hard skills. We would like our website and supporting images to reflect this.
We have worked throughout Africa and the Middle east, as well as Asia pacific. An international flavour to the website would also be great.
Background images on www.corvellpartnersglobal.example are a good example of what we are thinking of, though very open to fresh ideas.

Target Market(s)

Our customers are generally medium to large organisations who work internationally. We would like to also support more not for profits and non government organisations who work in hazardous environments

Industry/Entity Type

It Company

Number of Pages Required

5+ page

Font styles to use
Sans Serif

Requirements
Must have
• Easy to edit by non IT people
• Section for blogs/news updates
• Pages should include:
• (A) home page
• (B) about us
• (C) services
• (D) contact
• (E) insights
Nice to have
• An international and professional theme. Some gritty images that symbolise the risks associated with working in unstable environments, as well as some human ones and that of the environment
Should not have
• Cartoonish or generic images
• Not focus on traditional physical security aspects

```html
<!DOCTYPE html>
<html lang="en">
<head>
<meta charset="utf-8">
<title>Halvern Risk</title>
<link rel="stylesheet" href="https://fonts.googleapis.com/css2?family=Roboto+Condensed:wght@300;400;700&family=Open+Sans:wght@400;600&display=swap">
<style>
:root{
  --blue:#0f6fa3;
  --blue-dark:#0a4f78;
  --ink:#2a2a2a;
  --grey:#7a7a7a;
  --footer:#242424;
  --footer-bar:#1a1a1a;
  --white:#ffffff;
}
*{box-sizing:border-box;margin:0;padding:0}
html,body{width:1200px;height:2740px;overflow:hidden}
body{font-family:"Open Sans",sans-serif;color:var(--ink);background:var(--white);position:relative}

/* Hero */
.hero{position:absolute;top:0;left:0;width:1200px;height:732px;
  background:linear-gradient(180deg,#dfe8ee 0%,#b9c8d3 22%,#6f8596 50%,#3a4a58 78%,#27323c 100%)}
.hero-logo{position:absolute;left:40px;top:24px;display:flex;flex-direction:column;align-items:flex-start;gap:10px}
.hero-logo .dot{width:120px;height:120px;border-radius:50%;background:var(--blue)}
.hero-logo span{font-family:"Roboto Condensed",sans-serif;font-weight:700;font-size:30px;color:var(--blue-dark)}
.nav{position:absolute;top:60px;left:500px;width:640px;display:flex;justify-content:space-between;align-items:center}
.nav a{font-family:"Roboto Condensed",sans-serif;font-size:17px;color:#3d5566;text-decoration:none;padding:10px 24px;letter-spacing:.5px;border:2px solid transparent}
.nav a.active{border-color:var(--blue);border-radius:30px;background:rgba(255,255,255,.55);color:var(--blue-dark)}
.hero h1{position:absolute;top:388px;width:100%;text-align:center;font-family:"Roboto Condensed",sans-serif;font-weight:700;font-size:48px;color:var(--white);letter-spacing:1px;text-shadow:0 2px 6px rgba(0,0,0,.4)}
.hero p{position:absolute;top:452px;width:100%;text-align:center;font-family:"Roboto Condensed",sans-serif;font-size:38px;color:var(--white)}

/* Welcome */
.welcome{position:absolute;top:732px;left:0;width:1200px;height:208px;text-align:center}
.welcome h2{margin-top:30px;font-family:"Roboto Condensed",sans-serif;font-weight:300;font-size:56px;color:#666}
.welcome h2 b{font-weight:300;color:var(--blue)}
.rule{width:70px;height:3px;background:var(--blue);margin:10px auto 0}
.welcome p{width:760px;margin:22px auto 0;font-size:13px;line-height:22px;color:var(--grey)}

/* Services */
.services{position:absolute;top:940px;left:0;width:1200px;height:592px;
  background:linear-gradient(180deg,var(--blue) 0%,var(--blue-dark) 100%)}
.tab{position:absolute;left:440px;top:60px;width:320px;height:70px;background:#d8dde1;border-radius:35px;text-align:center;
  font-family:"Roboto Condensed",sans-serif;font-size:40px;line-height:70px;color:var(--ink)}
.svc{position:absolute;top:200px;width:360px;text-align:center;color:var(--white)}
.svc .ring{width:140px;height:140px;border-radius:50%;border:5px solid var(--white);margin:0 auto;display:flex;align-items:center;justify-content:center}
.svc .ring .core{width:110px;height:110px;border-radius:50%;background:var(--white);display:flex;align-items:center;justify-content:center}
.svc h3{margin-top:26px;font-family:"Roboto Condensed",sans-serif;font-weight:400;font-size:30px;line-height:38px;min-height:76px}
.svc p{margin:10px auto 0;width:290px;font-size:14px;line-height:23px;color:#d7e6ef}

/* Call to action */
.cta{position:absolute;top:1532px;left:0;width:1200px;height:316px;
  background:linear-gradient(180deg,#1f2427 0%,#2e3438 55%,#3c4246 100%);text-align:center;color:var(--white)}
.cta h2{margin-top:50px;font-family:"Roboto Condensed",sans-serif;font-weight:400;font-size:44px}
.cta p{width:640px;margin:14px auto 0;font-size:14px;line-height:23px;color:#d0d4d6}
.cta .btn{display:inline-block;margin-top:30px;padding:12px 36px;border:3px solid var(--white);border-radius:34px;font-family:"Roboto Condensed",sans-serif;font-size:30px}

/* News */
.news{position:absolute;top:1848px;left:0;width:1200px;height:572px;text-align:center}
.news h2{margin-top:40px;font-family:"Roboto Condensed",sans-serif;font-weight:300;font-size:56px;color:#666}
.news h2 b{font-weight:300;color:var(--blue)}
.card{position:absolute;top:160px;width:312px;height:370px;border:1px solid #dde3e7;text-align:left;background:var(--white)}
.card .photo{height:150px;background:linear-gradient(135deg,#7fa7c4,#3d6a8c 60%,#25455e)}
.card .photo.b{background:linear-gradient(135deg,#b9c4cc,#6c7d8a 55%,#3a4853)}
.card .photo.c{background:linear-gradient(180deg,#e9d6b6,#a9a49a 55%,#4d4d4d)}
.card h4{margin:14px 16px 0;font-family:"Roboto Condensed",sans-serif;font-weight:400;font-size:24px;color:var(--blue)}
.card .meta{margin:4px 16px 0;font-size:11px;color:#999}
.card p{margin:12px 16px 0;font-size:13px;line-height:21px;color:var(--grey)}
.card .foot{position:absolute;left:16px;right:16px;bottom:14px;display:flex;justify-content:space-between;font-size:13px;color:#666}
.card .foot span{display:flex;align-items:center;gap:6px}

/* Footer */
.footer{position:absolute;top:2420px;left:0;width:1200px;height:276px;background:var(--footer);color:#ccc}
.col{position:absolute;top:30px}
.col h5{font-family:"Roboto Condensed",sans-serif;font-weight:400;font-size:28px;color:var(--white);margin-bottom:16px}
.col ul{list-style:none;font-size:13px;line-height:28px}
.col ul li:first-child{color:var(--white)}
.col p{font-size:13px;line-height:22px;width:300px}
.field{margin-top:18px;width:210px;height:36px;background:#3a3a3a;border:1px solid #4a4a4a;font-size:12px;line-height:34px;padding-left:12px;color:#999}
.subscribe{margin-top:16px;display:inline-block;background:var(--blue);color:var(--white);font-size:15px;padding:8px 22px}
.contact li{display:flex;align-items:center;gap:10px}
.social{display:flex;gap:20px;margin-top:14px}
.social i{width:16px;height:16px;border-radius:50%;background:#aaa;display:block}
.bar{position:absolute;top:2696px;left:0;width:1200px;height:44px;background:var(--footer-bar);text-align:center;font-size:12px;line-height:44px;color:#aaa}
.bar b{color:var(--white)}
</style>
</head>
<body>

<header class="hero" role="img" aria-label="City skyline of tall towers under a pale sky">
  <div class="hero-logo"><div class="dot"></div><span>Halvern Risk</span></div>
  <nav class="nav">
    <a class="active">HOME</a><a>ABOUT</a><a>SERVICES</a><a>CONTACT</a><a>INSIGHTS</a>
  </nav>
  <h1>OPERATIONAL RISK MANAGEMENT</h1>
  <p>Ethical And Sustainable Manner</p>
</header>

<section class="welcome">
  <h2>Welcome to <b>Halvern Risk</b></h2>
  <div class="rule"></div>
  <p>Lorem Ipsum is simply dummy text of the printing and typesetting industry. Lorem Ipsum has been the industry's standard dummy text ever since the 1500s, when an unknown printer took a galley of type and scrambled it to make a type specimen book.</p>
</section>

<section class="services">
  <div class="tab">Our Services</div>

  <div class="svc" style="left:60px">
    <div class="ring"><div class="core">
      <svg width="60" height="54" viewBox="0 0 64 58"><path d="M32 4 L60 54 H4 Z" fill="none" stroke="#555" stroke-width="5" stroke-linejoin="round"/><rect x="29" y="20" width="6" height="18" rx="2" fill="#555"/><circle cx="32" cy="45" r="3.5" fill="#555"/></svg>
    </div></div>
    <h3>Crisis and emergency<br>management</h3>
    <p>Lorem Ipsum is simply dummy text of the printing and typesetting industry. Lorem Ipsum has been the industry.</p>
  </div>

  <div class="svc" style="left:420px">
    <div class="ring"><div class="core">
      <svg width="66" height="50" viewBox="0 0 70 54" fill="#555"><circle cx="35" cy="14" r="9"/><path d="M20 46 a15 15 0 0 1 30 0 Z"/><circle cx="14" cy="20" r="7"/><path d="M2 46 a12 12 0 0 1 18 -10 v10 Z"/><circle cx="56" cy="20" r="7"/><path d="M68 46 a12 12 0 0 0 -18 -10 v10 Z"/></svg>
    </div></div>
    <h3>Community Engagement</h3>
    <p>Lorem Ipsum is simply dummy text of the printing and typesetting industry. Lorem Ipsum has been the industry.</p>
  </div>

  <div class="svc" style="left:780px">
    <div class="ring"><div class="core">
      <svg width="52" height="60" viewBox="0 0 56 64"><path d="M28 3 L52 12 V32 C52 48 40 57 28 61 C16 57 4 48 4 32 V12 Z" fill="#555"/><path d="M17 32 L25 40 L40 24" fill="none" stroke="#fff" stroke-width="5" stroke-linecap="round" stroke-linejoin="round"/></svg>
    </div></div>
    <h3>Safety and Security</h3>
    <p>Lorem Ipsum is simply dummy text of the printing and typesetting industry. Lorem Ipsum has been the industry.</p>
  </div>
</section>

<section class="cta" role="img" aria-label="Darkened photo of a business team at a meeting table">
  <h2>Operational Risk Management</h2>
  <p>Lorem Ipsum is simply dummy text of the printing and typesetting industry. Lorem Ipsum has been the industry's standard dummy text ever since the 1500s.</p>
  <div class="btn">Request A Call Back</div>
</section>

<section class="news">
  <h2>Latest <b>News</b></h2>
  <div class="rule"></div>

  <article class="card" style="left:76px">
    <div class="photo" role="img" aria-label="Glass office towers seen from below"></div>
    <h4>News Title</h4>
    <div class="meta">Posted On 16 Aug by Admin</div>
    <p>Lorem Ipsum is simply dummy text of the printing and typesetting industry. Lorem Ipsum has been the industry.</p>
    <div class="foot"><span>Share <svg width="14" height="12" viewBox="0 0 14 12"><path d="M1 6 H12 M8 2 L12 6 L8 10" fill="none" stroke="#666" stroke-width="1.6"/></svg></span><span>Comment <svg width="16" height="14" viewBox="0 0 16 14"><path d="M2 2 H14 V10 H7 L3 13 V10 H2 Z" fill="none" stroke="var(--blue)" stroke-width="1.6"/></svg></span></div>
  </article>

  <article class="card" style="left:444px">
    <div class="photo b" role="img" aria-label="Business people shaking hands in an office"></div>
    <h4>News Title</h4>
    <div class="meta">Posted On 16 Aug by Admin</div>
    <p>Lorem Ipsum is simply dummy text of the printing and typesetting industry. Lorem Ipsum has been the industry.</p>
    <div class="foot"><span>Share <svg width="14" height="12" viewBox="0 0 14 12"><path d="M1 6 H12 M8 2 L12 6 L8 10" fill="none" stroke="#666" stroke-width="1.6"/></svg></span><span>Comment <svg width="16" height="14" viewBox="0 0 16 14"><path d="M2 2 H14 V10 H7 L3 13 V10 H2 Z" fill="none" stroke="var(--blue)" stroke-width="1.6"/></svg></span></div>
  </article>

  <article class="card" style="left:812px">
    <div class="photo c" role="img" aria-label="Group of colleagues standing before a bright window"></div>
    <h4>News Title</h4>
    <div class="meta">Posted On 16 Aug by Admin</div>
    <p>Lorem Ipsum is simply dummy text of the printing and typesetting industry. Lorem Ipsum has been the industry.</p>
    <div class="foot"><span>Share <svg width="14" height="12" viewBox="0 0 14 12"><path d="M1 6 H12 M8 2 L12 6 L8 10" fill="none" stroke="#666" stroke-width="1.6"/></svg></span><span>Comment <svg width="16" height="14" viewBox="0 0 16 14"><path d="M2 2 H14 V10 H7 L3 13 V10 H2 Z" fill="none" stroke="var(--blue)" stroke-width="1.6"/></svg></span></div>
  </article>
</section>

<footer class="footer">
  <div class="col" style="left:76px">
    <h5>Useful Links</h5>
    <ul><li>HOME</li><li>ABOUT</li><li>SERVICES</li><li>CONTACT</li><li>INSIGHTS</li></ul>
  </div>
  <div class="col" style="left:444px">
    <h5>Newsletter</h5>
    <p>Lorem Ipsum is simply dummy text of the printing and typesetting.</p>
    <div class="field">Enter Email Id</div>
    <div class="subscribe">Subscribe</div>
  </div>
  <div class="col contact" style="left:812px">
    <h5>Contact Us</h5>
    <ul>
      <li><svg width="12" height="16" viewBox="0 0 12 16"><path d="M6 1 A5 5 0 0 1 11 6 C11 10 6 15 6 15 C6 15 1 10 1 6 A5 5 0 0 1 6 1 Z" fill="var(--blue)"/><circle cx="6" cy="6" r="2" fill="#242424"/></svg>Lorem Ipsum is simply dummy text</li>
      <li><svg width="14" height="14" viewBox="0 0 14 14"><path d="M3 1 L5.5 4 L4 6 C5 8 6 9 8 10 L10 8.5 L13 11 L11 13 C6 13 1 8 1 3 Z" fill="var(--blue)"/></svg>555 014 2093</li>
      <li><svg width="14" height="11" viewBox="0 0 14 11"><rect x="0.8" y="0.8" width="12.4" height="9.4" fill="none" stroke="var(--blue)" stroke-width="1.6"/><path d="M1 1 L7 6 L13 1" fill="none" stroke="var(--blue)" stroke-width="1.6"/></svg>info@halvernrisk.example</li>
    </ul>
    <div class="social"><i></i><i></i><i></i></div>
  </div>
</footer>
<div class="bar">© <b>HALVERN RISK</b> 2017, All Rights reserved.</div>

</body>
</html>
```